business card - for laser marking

I need design (curve) for my business card (make with laser) size 85mm x 55mm. How it look business card with laser marking see attached picture.

color:
Background: white
text and icons black

Please include: one side
1. dominik vrhovec - direktor
2. phone: +386(0)41 726 193
+386(0)592 817 06
3. info@zlatorez.example
4. faecebook.com/Zlatorez.Ex
5. KP-ATELJE, Dominik Vrhovec s.p.
Brezova ulica 17, 1000 Ljubljana, SI
6. logo

Please include: second side
1. logo
2. www.zlatorez.example
3. Lasersko graviranje
ovitki telefonov, ohišja telefonov / tablic, nakit, ure, alu vizitke, dog-tagi, kemični svinčniki, orodja, noži, vžigalniki

Industry/Entity Type

Business

Contact Information for Business Card

Please include: one side
+386(0)592 817 06
3. info@zlatorez.example
6. logo

1. logo
2. www.zlatorez.example
3. Lasersko graviranje

Colors
000000
ffffff

Requirements
Must have
• I need design (curve) for my business card (make with laser) size 85mm x 55mm. How it look business card with laser marking see attached picture.
• color:
• Background: white
• text and icons black
• Please include: one side
• 1. dominik vrhovec - direktor
• 2. phone: +386(0)41 726 193
• +386(0)592 817 06
• 3. info@zlatorez.example
• 4. faecebook.com/Zlatorez.Ex
• 5. KP-ATELJE, Dominik Vrhovec s.p.
• Brezova ulica 17, 1000 Ljubljana, SI
• 6. logo
• Please include: second side
• 1. logo
• 2. www.zlatorez.example
• 3. Lasersko graviranje
• ovitki telefonov, ohišja telefonov / tablic, nakit, ure, alu vizitke, dog-tagi, kemični svinčniki, orodja, noži, vžigalniki

```html
<!DOCTYPE html>
<html lang="sl">
<head>
<meta charset="utf-8">
<title>Zlatorez – vizitka</title>
<link rel="stylesheet" href="https://fonts.googleapis.com/css2?family=Roboto:wght@400;500;700&family=Roboto+Condensed:wght@700&display=swap">
<style>
  :root {
    --stage: #e6e3df;
    --card: #ffffff;
    --ink: #000000;
  }
  * { margin: 0; padding: 0; box-sizing: border-box; }
  html, body {
    width: 1200px; height: 960px; overflow: hidden;
    background: var(--stage);
    font-family: "Roboto", Arial, sans-serif;
    color: var(--ink);
  }
  .canvas { position: relative; width: 1200px; height: 960px; }

  .card { position: absolute; height: 343px; background: var(--card); box-shadow: 0 3px 6px rgba(0,0,0,.25); overflow: hidden; }
  .card--front { left: 314px; top: 113px; width: 572px; }
  .card--back { left: 312px; top: 472px; width: 599px; }

  .name-bar { position: absolute; left: 0; top: 43px; width: 13px; height: 41px; background: var(--ink); }
  .person-name {
    position: absolute; left: 39px; top: 41px;
    font-family: "Roboto Condensed", "Arial Narrow", sans-serif;
    font-weight: 700; font-size: 21px; letter-spacing: .2px; line-height: 26px;
  }
  .person-role {
    position: absolute; left: 39px; top: 68px;
    font-family: "Roboto Condensed", "Arial Narrow", sans-serif;
    font-weight: 700; font-size: 15px; line-height: 19px;
  }

  .contact-list { position: absolute; left: 39px; top: 236px; list-style: none; }
  .contact-list li {
    display: flex; align-items: center; height: 19px;
    font-size: 14px;
  }
  .contact-list svg { width: 13px; height: 13px; margin-right: 9px; flex: none; }

  .brand-name--front {
    position: absolute; left: 384px; top: 170px; width: 180px; text-align: center;
    font-weight: 700; font-size: 25px; letter-spacing: 1px; line-height: 30px;
  }

  .company-address {
    position: absolute; right: 8px; top: 276px; text-align: right;
    font-style: normal; font-size: 14px; line-height: 19px;
  }

  .brand-name--back {
    position: absolute; left: 0; right: 0; top: 146px; text-align: center;
    font-weight: 700; font-size: 44px; letter-spacing: 2px; line-height: 52px;
  }
  .services {
    position: absolute; left: 0; right: 0; top: 226px; text-align: center;
    font-size: 14px; line-height: 18.5px;
  }
  .website {
    position: absolute; left: 0; right: 0; top: 302px; text-align: center;
    font-weight: 500; font-size: 15px; line-height: 18px;
  }
</style>
</head>
<body>
<main class="canvas">

  <section class="card card--front" aria-label="Sprednja stran vizitke">
    <div class="name-bar"></div>
    <h1 class="person-name">DOMINIK VRHOVEC</h1>
    <p class="person-role">DIREKTOR</p>

    <ul class="contact-list">
      <li>
        <svg viewBox="0 0 16 16" aria-hidden="true"><path fill="var(--ink)" d="M3.6 1.2l2.3 2.6-1.3 1.9c.9 2 2.6 3.8 4.7 4.8l1.9-1.3 2.6 2.3-1.3 2.3C7.7 14.6 1.4 8.3 1.2 2.5z"/></svg>
        +386(0)592 817 06
      </li>
      <li>
        <svg viewBox="0 0 16 16" aria-hidden="true"><rect x="4" y="1" width="8" height="14" rx="1.5" fill="none" stroke="var(--ink)" stroke-width="1.8"/><circle cx="8" cy="12.3" r="1" fill="var(--ink)"/></svg>
        +386(0)41 726 193
      </li>
      <li>
        <svg viewBox="0 0 16 16" aria-hidden="true"><rect x="1" y="3.5" width="14" height="9" fill="var(--ink)"/><path d="M1.5 4l6.5 5 6.5-5" fill="none" stroke="var(--card)" stroke-width="1.2"/></svg>
        info@zlatorez.example
      </li>
      <li>
        <svg viewBox="0 0 16 16" aria-hidden="true"><rect x="1.5" y="1.5" width="13" height="13" fill="var(--ink)"/></svg>
        Zlatorez.Ex
      </li>
    </ul>

    <p class="brand-name--front">ZLATOREZ</p>

    <address class="company-address">
      KP-ATELJE, Dominik Vrhovec s.p.<br>
      Brezova ulica 17, 1000 Ljubljana, SI
    </address>
  </section>

  <section class="card card--back" aria-label="Zadnja stran vizitke">
    <p class="brand-name--back">ZLATOREZ</p>
    <p class="services">
      Lasersko graviranje<br>
      ovitki telefonov, ohišja telefonov / tablic, nakit, ure, alu vizitke<br>
      dog-tagi, kemični svinčniki, orodja, noži, vžigalniki
    </p>
    <p class="website">www.zlatorez.example</p>
  </section>

</main>
</body>
</html>
```